Zielgruppe
Beratung und Live-Kommunikation
Aufgabenstellung
- Re-Design vom Firmenlogo und Briefpapier
- Anpassung/ Abwandlung der vorhandenen Elemente (Briefkopf). Anordnung, Schrift, etc.
- Ideen, wie man den Inhalt (den Tätigkeitsbereich) ggfs. grafisch ansprechend als Logo darstellen kann.
- Klare Linien, symmetrisch. Schwarz-weiß/keine Farbe
- Briefpapier auf *.doc Basis, kein randloser Druck
- derzeitiger Stil siehe www.buehnenwerkraum.de

```html
<!DOCTYPE html>
<html lang="de">
<head>
<meta charset="utf-8">
<title>Visitenkarten – Herbrecht Live</title>
<link rel="stylesheet" href="https://fonts.googleapis.com/css2?family=Arimo:wght@400&display=swap">
<style>
  :root {
    --backdrop: #1f1f1f;
    --card: #ffffff;
    --block: #b3b3b3;
    --label: #555555;
    --value: #9f9f9f;
    --accent-word: #4a4a4a;
  }
  * { margin: 0; padding: 0; box-sizing: border-box; }
  html, body {
    width: 1200px; height: 801px; overflow: hidden;
    background: var(--backdrop);
    font-family: "Arimo", Helvetica, Arial, sans-serif;
  }
  .card {
    position: absolute; top: 226px;
    width: 540px; height: 349px;
    background: var(--card);
  }
  .card--contact { left: 40px; }
  .card--services { left: 620px; }

  .block { position: absolute; background: var(--block); }

  /* contact side */
  .contact-line {
    position: absolute; left: 97px;
    font-size: 13.5px; line-height: 1; white-space: nowrap;
    color: var(--value); letter-spacing: 0.2px;
  }
  .contact-line .label { color: var(--label); }
  .contact-line.name { color: var(--label); }
  .block--left { left: 25px; top: 160px; width: 57px; height: 71px; }
  .block--right { left: 373px; top: 160px; width: 143px; height: 71px; }

  /* services side */
  .company {
    position: absolute; left: 28px; top: 184px;
    color: var(--label); font-size: 20px; line-height: 1;
    letter-spacing: 0.5px; white-space: nowrap;
  }
  .services {
    position: absolute; left: 316px; top: 133px;
    list-style: none; color: var(--value);
    font-size: 15.5px; line-height: 22.5px; letter-spacing: 3px;
    white-space: nowrap;
  }
  .services .strong { color: var(--accent-word); }
  .block--mark { left: 475px; top: 160px; width: 40px; height: 71px; }
</style>
</head>
<body>

<section class="card card--contact" aria-label="Visitenkarte Vorderseite">
  <div class="block block--left"></div>
  <div class="block block--right"></div>
  <p class="contact-line name" style="top:67px">Jonas Herbrecht</p>
  <p class="contact-line" style="top:94px">Lindenweg 4b</p>
  <p class="contact-line" style="top:114px">50321 Brühlbach</p>
  <p class="contact-line" style="top:155px"><span class="label">Kontakt</span></p>
  <p class="contact-line" style="top:175px"><span class="label">T.:</span> +49 (0) 170 318 552 04</p>
  <p class="contact-line" style="top:195px"><span class="label">F.:</span> +49 (0) 221 407 615 38</p>
  <p class="contact-line" style="top:215px"><span class="label">E-Mail:</span> herbrecht@buehnenwerkraum.de</p>
  <p class="contact-line" style="top:255px"><span class="label">Internet</span></p>
  <p class="contact-line" style="top:276px"><span class="label">www.</span>buehnenwerkraum.de</p>
</section>

<section class="card card--services" aria-label="Visitenkarte Rückseite">
  <p class="company">Herbrecht Live</p>
  <ul class="services">
    <li>Konzeption</li>
    <li>organisation</li>
    <li>corporate <span class="strong">event</span></li>
    <li class="strong">management</li>
    <li>entrertainment</li>
    <li>ausstellungen</li>
  </ul>
  <div class="block block--mark"></div>
</section>

</body>
</html>
```